Website design for Cambridge based systematic hedge fund

We have run previous craftmosaic competitions to design our company logo, business cards and the styling of our presentation deck (see attached files).
As the final step we are looking to get a website designed that is thematically consistent with these existing elements of our branding.
You can find some of our competitors websites below:
https://www.quelmarsh.example/
https://www.fenloor.example/
https://www.pyvart.example/
https://www.dulvet.example/
https://www.orbelmfunds.example/
https://www.valtrigo.example/
https://www.meskilfunds.example/home
We would like to have a website that works well on both mobile devices and desktops. Either just as one page that can be scrolled down, with links at the top that skips to certain sections, or a few separate pages that can be navigated by a top menu.
It should look professional, we are not after lots of animations or unnecessary transitions, and in particular the website must be smooth to navigate. We would like to avoid having peoples of people, we are happy to make use of elements from the presentation (for example the style of the cover slide, or the section slides with the faded bridge in the background), or 'financial' style images.
We would like to have the following sections for now. For some of these some example text has been provided, final text may change but it will be of similar length. For the other sections we are happy to just have template text for now. At the moment we are mainly interested to see styles/layouts as words can be added easily afterwards:
1) We will need a disclaimer pop up the first time someone visits the site (see for example the meskilfunds example).
2) Top page - company name, then in larger text "Bringing AI and Statistical Inference to Financial Markets", and somewhere in smaller text "Harlow Vectors is a quantitative asset manager with the singular focus of delivering algorithmic strategies that work"
3) "About us" section: will describe us as a company, details our approach, company values, and explains the company logo.
Example text:
"We deliver consistent alpha across liquid markets through the application of proprietary IP in Bayesian inference, machine learning and artificial intelligence. We are a multi-disciplinary team founded by experienced finance professionals from premier institutions, leading academics from the Thornbury Stellar Unit at Ashmere College and world-class software engineers.
Our logo portrays a sillhoute of the lattice walkway at Ashmere College. Our unique scientific approach allows us to bridge cutting-edge mathematical research and computing expertise with financial knowledge to bring algorithmns that work to liquid markets"
4) Hiring section, detailing our culture, what we are looking for.
Example text:
"We are always looking for exceptional talent to join our entrepreneurial team. We are looking for individuals who are creative thinkers, can demonstrate analytical rigour and are passionate about the intersection of science, finance and technology.
We prioritise having a company culture that promotes sharing ideas in a safe, collaborative research environment. We make sure that every member of the team has the oppertunity to explore their own ideas through weekly 'innovation time', and ensure that everyone gets the support they need to continue to grow as individuals within the company."
5) A section for news/press releases
6) Contact us area at the bottom with office location and email. We will need to list 3 addresses for our Cambridge, London and Singapore offices, along with a couple of contact emails or phone numbers
7) A client login button at the top that will take them to a different website (unrelated to this one).

```html
<!DOCTYPE html>
<html lang="en">
<head>
<meta charset="utf-8">
<title>Harlow Vectors</title>
<link href="https://fonts.googleapis.com/css2?family=Montserrat:wght@300;400;500;600;700&family=Open+Sans:wght@400;600&display=swap" rel="stylesheet">
<style>
:root{
  --navy:#03234d;
  --deep:#062f63;
  --blue:#0a4a8f;
  --accent:#4a90d9;
  --sky:#5b9be0;
  --ink:#1b2a3a;
  --grey:#7a8591;
  --paper:#ffffff;
  --soft:#f3f3f3;
  --panel:#dcdcdc;
}
*{box-sizing:border-box;margin:0;padding:0}
html,body{width:1200px;height:4402px;overflow:hidden}
body{position:relative;font-family:"Open Sans",sans-serif;color:var(--ink);background:var(--paper)}
.abs{position:absolute}
.head{font-family:"Montserrat",sans-serif}

/* hero */
.hero{left:0;top:0;width:1200px;height:744px;background:radial-gradient(circle at 80% 40%,#0f5aa8,#062f63 60%,#031f45)}
.nav a{position:absolute;top:40px;font:500 13px "Montserrat",sans-serif;color:#fff;text-decoration:none;letter-spacing:.5px}
.nav .active{border-bottom:2px solid #fff;padding-bottom:8px}
.login{left:985px;top:34px;width:93px;height:26px;border:1px solid #fff;color:#fff;font:500 11px "Montserrat",sans-serif;display:flex;align-items:center;justify-content:center}
.hero-title{left:111px;top:276px;color:#fff;font:700 40px/48px "Montserrat",sans-serif}
.hero-title .light{font-weight:300}
.learn{left:113px;top:441px;width:180px;height:43px;border:2px solid #fff;color:#fff;font:600 13px "Montserrat",sans-serif;display:flex;align-items:center;justify-content:center}
.arrow{top:350px}

/* about */
.about{left:0;top:744px;width:1200px;height:598px;background:#fff}
.globe{left:-60px;top:744px;width:620px;height:598px;border-radius:0 50% 50% 0;background:radial-gradient(circle at 40% 45%,#1a6fc0,#0a3f7d 60%,#052651)}
.eyebrow{font:400 16px "Montserrat",sans-serif;letter-spacing:4px;color:var(--blue)}
.h2{font:700 30px "Montserrat",sans-serif;color:var(--navy)}
.h2 span{color:var(--sky)}
.h2 .thin{font-weight:300}
.bar{width:80px;height:3px;background:var(--blue)}
.copy{font-size:13px;line-height:21.5px;color:#4b5561}

/* approach */
.approach{left:0;top:1342px;width:1200px;height:558px;background:linear-gradient(#062f63,#042753)}
.step{width:240px;text-align:center;color:#fff}
.step .ring{width:92px;height:92px;margin:0 auto;border-radius:50%;border:3px solid var(--sky);display:flex;align-items:center;justify-content:center;background:#0a4a8f}
.step h4{font:700 13px "Montserrat",sans-serif;margin-top:36px;letter-spacing:.5px}
.step p{font-size:11px;line-height:18px;color:#b9c8da;margin-top:12px}

/* hiring */
.photo{border-radius:0}
.card{background:#fff;box-shadow:6px 6px 0 var(--blue),0 4px 20px rgba(0,0,0,.15);padding:56px 50px}
.card h3{font:700 20px "Montserrat",sans-serif;color:var(--navy)}
.card h3 span{color:var(--sky)}
.card p{margin-top:28px;font-size:13px;line-height:25px;color:#56606b}

/* news */
.news{width:300px;height:350px;background:#fff;box-shadow:0 2px 10px rgba(0,0,0,.12)}
.news .img{height:181px}
.news .date{margin:30px 30px 0;font-size:10px;color:var(--sky)}
.news h5{margin:8px 30px 0;font:600 14px/18px "Montserrat",sans-serif;color:var(--navy)}
.news p{margin:14px 30px 0;font-size:10px;line-height:16px;color:#8892a0}

/* contact */
.contact{left:0;top:3577px;width:1200px;height:559px;background:linear-gradient(#062f63,#073670)}
.c-line{color:#fff;font-size:15px;display:flex;align-items:center;gap:18px}
.office h6{font:600 15px "Montserrat",sans-serif;color:#fff}
.office p{font-size:12px;line-height:20px;color:#c8d5e6;margin-top:4px}
.pin{width:66px;height:66px;border-radius:50%;background:#fff;display:flex;align-items:center;justify-content:center}

/* footer */
.footer{left:0;top:4136px;width:1200px;height:266px;background:#041f45}
.f-col h6{font:600 11px "Montserrat",sans-serif;color:#fff;letter-spacing:1px}
.f-col p{font-size:11px;line-height:19px;color:#9fb0c6;margin-top:10px}
.f-div{width:2px;height:22px;background:#9fb0c6}

/* disclaimer */
.shade{left:0;top:0;width:1200px;height:4402px;background:rgba(3,38,86,.78)}
.modal{left:219px;top:150px;width:782px;height:575px;background:var(--soft);border:1px solid #ccc}
.brand{left:36px;top:38px;font:700 26px "Montserrat",sans-serif;color:var(--blue);display:flex;align-items:center;gap:10px}
.brand i{width:14px;height:14px;background:var(--blue);display:block}
.m-title{left:33px;top:128px;font:700 28px "Montserrat",sans-serif;color:#111;letter-spacing:.5px}
.m-title span{color:var(--sky)}
.m-intro{left:38px;top:170px;width:700px;font-size:13px;line-height:20px;color:#222}
.terms{left:30px;top:237px;width:727px;height:153px;background:#fff;border:1px solid #bbb}
.terms .num{left:32px;top:22px;font:700 20px "Montserrat",sans-serif;color:var(--sky)}
.terms h4{left:52px;top:23px;font:700 14px "Montserrat",sans-serif;color:#111}
.terms p{left:52px;top:50px;width:630px;font-size:12px;line-height:19px;color:#333}
.scroll{left:712px;top:0;width:12px;height:151px;background:#f0f0f0}
.btn{height:40px;border-radius:20px;font:700 13px "Montserrat",sans-serif;display:flex;align-items:center;justify-content:center;letter-spacing:.5px}
.accept{left:205px;top:407px;width:171px;background:var(--sky);color:#fff}
.decline{left:386px;top:407px;width:171px;border:2px solid #111;color:#111;background:#fff}
.cookies{left:26px;top:458px;width:735px;height:89px;background:var(--panel);border:1px solid #aaa;padding:16px 12px;font-size:11.5px;line-height:17px;color:#111}
.cookies b{font:700 13px "Montserrat",sans-serif;display:block}
</style>
</head>
<body>

<!-- hero -->
<section class="abs hero" role="img" aria-label="Dark blue network of connected points background"></section>
<nav class="nav">
  <a class="active" style="left:347px">ABOUT US</a>
  <a style="left:475px">APPROACH</a>
  <a style="left:608px">CULTURE</a>
  <a style="left:724px">HIRING</a>
  <a style="left:833px">CONTACT US</a>
</nav>
<div class="abs login">LOGIN &#8594;</div>
<h1 class="abs hero-title"><span class="light">BRINGING AI AND</span><br>STATISTICAL INFERENCE TO<br>FINANCIAL MARKETS</h1>
<div class="abs learn">LEARN MORE</div>
<svg class="abs arrow" style="left:38px" width="24" height="36"><path d="M20 2 4 18l16 16" stroke="#fff" stroke-width="3" fill="none"/></svg>
<svg class="abs arrow" style="left:1157px" width="24" height="36"><path d="M4 2l16 16L4 34" stroke="#fff" stroke-width="3" fill="none"/></svg>

<!-- about -->
<section class="abs about"></section>
<div class="abs globe" role="img" aria-label="Glowing blue globe with data network"></div>
<div class="abs eyebrow" style="left:656px;top:856px">WHO WE ARE</div>
<h2 class="abs h2" style="left:660px;top:880px">ABOUT <span>HARLOW</span></h2>
<div class="abs bar" style="left:660px;top:922px"></div>
<p class="abs copy" style="left:660px;top:952px;width:440px">We deliver consistent alpha across liquid markets through the application of proprietary IP in Bayesian inference, machine learning and artificial intelligence. We are a multi-disciplinary team founded by experienced finance professionals from premier institutions, leading academics from the Thornbury Stellar Unit at Ashmere College and world-class software engineers.<br><br>Our logo portrays a silhouette of the lattice walkway at Ashmere College. Our unique scientific approach allows us to bridge cutting-edge mathematical research and computing expertise with financial knowledge to bring algorithms that work to liquid markets.</p>

<!-- approach -->
<section class="abs approach"></section>
<h2 class="abs h2" style="left:0;width:1200px;text-align:center;top:1410px;color:#fff"><span class="thin" style="color:#fff">OUR </span><span>APPRAOCH</span></h2>
<div class="abs bar" style="left:570px;top:1453px;width:60px;background:#fff"></div>
<svg class="abs" style="left:310px;top:1480px" width="590" height="100"><g stroke="#6d93c0" stroke-width="1.5" fill="none"><path d="M290 0v52M6 90V70q0-18 18-18h532q18 0 18 18v20M290 52v38"/></g></svg>
<div class="abs step" style="left:196px;top:1591px"><div class="ring"><svg width="40" height="40" fill="none" stroke="#fff" stroke-width="2"><rect x="6" y="8" width="28" height="18"/><path d="M6 8l14 10 14-10"/><circle cx="10" cy="33" r="3"/><circle cx="20" cy="33" r="3"/><circle cx="30" cy="33" r="3"/></svg></div><h4>LOREM IPSUM DOLOR SIT</h4><p>Lorem ipsum dolor sit amet consectetur<br>adipiscing elit sed diam nonum</p></div>
<div class="abs step" style="left:481px;top:1591px"><div class="ring"><svg width="40" height="40" fill="none" stroke="#fff" stroke-width="2"><rect x="4" y="6" width="14" height="10"/><rect x="22" y="6" width="14" height="10"/><rect x="4" y="24" width="14" height="10"/><circle cx="29" cy="29" r="6"/><path d="M26 29l2 2 4-4"/></svg></div><h4>LOREM IPSUM DOLOR SIT</h4><p>Lorem ipsum dolor sit amet consectetur<br>adipiscing elit sed diam nonum</p></div>
<div class="abs step" style="left:764px;top:1591px"><div class="ring"><svg width="40" height="40" fill="none" stroke="#fff" stroke-width="2"><path d="M4 34h32M8 34V24M16 34V18M24 34V22M32 34V10"/><path d="M6 20l10-8 8 6 10-10"/></svg></div><h4>LOREM IPSUM DOLOR SIT</h4><p>Lorem ipsum dolor sit amet consectetur<br>adipiscing elit sed diam nonum</p></div>

<!-- hiring -->
<h2 class="abs h2" style="left:0;width:1200px;text-align:center;top:1972px"><span class="thin" style="color:var(--sky)">OUR </span>HIRING</h2>
<div class="abs bar" style="left:564px;top:2016px;width:76px"></div>
<div class="abs photo" style="left:150px;top:2078px;width:508px;height:386px;background:linear-gradient(160deg,#0a3f80,#04214a)" role="img" aria-label="Blue financial bar chart visual"></div>
<div class="abs card" style="left:610px;top:2121px;width:446px;height:306px"><h3>OUR <span>CULTURE</span></h3><p>We are always looking for exceptional talent to join our entrepreneurial team. We are looking for individuals who are creative thinkers, can demonstrate analytical rigour and are passionate about the intersection of science, finance and technology.</p></div>
<div class="abs photo" style="left:538px;top:2509px;width:508px;height:386px;background:linear-gradient(200deg,#0d5bad,#04264f)" role="img" aria-label="Blue digital data stream visual"></div>
<div class="abs card" style="left:161px;top:2552px;width:446px;height:304px"><h3>WHAT WE ARE <span>LOOKING FOR</span></h3><p>We prioritise having a company culture that promotes sharing ideas in a safe, collaborative research environment. We make sure that every member of the team has the opportunity to explore their own ideas through weekly 'innovation time', and ensure that everyone gets the support they need to continue to grow as individuals within the company.</p></div>

<!-- news -->
<h2 class="abs h2" style="left:0;width:1200px;text-align:center;top:3055px"><span class="thin" style="color:var(--sky)">LATEST </span>NEWS</h2>
<div class="abs news" style="left:138px;top:3141px"><div class="img" style="background:linear-gradient(135deg,#d8e3ef,#7f9bbb)" role="img" aria-label="Financial documents on desk"></div><div class="date">10 AUG 2021</div><h5>Lorem ipsum dolor sit amet, consectetur adipiscing elit</h5><p>Sed diam nonummy nibh euismod tincidunt ut laoreet dolore magna aliquam erat volutpat ut wisi enim.</p></div>
<div class="abs news" style="left:456px;top:3141px"><div class="img" style="background:linear-gradient(135deg,#0c4e96,#031f45)" role="img" aria-label="Blue digital city lights"></div><div class="date">10 AUG 2021</div><h5>Lorem ipsum dolor sit amet, consectetur adipiscing elit</h5><p>Sed diam nonummy nibh euismod tincidunt ut laoreet dolore magna aliquam erat volutpat ut wisi enim.</p></div>
<div class="abs news" style="left:774px;top:3141px"><div class="img" style="background:linear-gradient(135deg,#1f5f9f,#072d5c)" role="img" aria-label="Stock market chart screen"></div><div class="date">10 AUG 2021</div><h5>Lorem ipsum dolor sit amet, consectetur adipiscing elit</h5><p>Sed diam nonummy nibh euismod tincidunt ut laoreet dolore magna aliquam erat volutpat ut wisi enim.</p></div>

<!-- contact -->
<section class="abs contact"></section>
<h2 class="abs h2" style="left:147px;top:3695px;color:#fff;font-size:34px">CONTACT <span class="thin" style="color:#fff">US</span></h2>
<p class="abs" style="left:149px;top:3770px;width:360px;font-size:13px;line-height:19px;color:#c8d5e6">Lorem ipsum dolor sit amet, consectetur adipiscing elit, sed do eiusmod tempor incididunt ut labore et dolore magna aliqua. Ut enim ad.</p>
<div class="abs c-line" style="left:150px;top:3862px"><svg width="22" height="22" fill="#fff"><path d="M5 2l4 0 2 5-3 2a12 12 0 0 0 5 5l2-3 5 2v4c0 1-1 2-2 2A17 17 0 0 1 3 4c0-1 1-2 2-2z"/></svg>(144) 555 0142</div>
<div class="abs c-line" style="left:150px;top:3902px"><svg width="22" height="16" fill="#fff"><path d="M0 0h22v16H0z"/><path d="M0 0l11 9 11-9" stroke="#073670" stroke-width="2" fill="none"/></svg>enquiry@harlowvectors.example</div>
<div class="abs c-line" style="left:150px;top:3942px"><svg width="22" height="16" fill="#fff"><path d="M0 0h22v16H0z"/><path d="M0 0l11 9 11-9" stroke="#073670" stroke-width="2" fill="none"/></svg>info@harlowvectors.example</div>
<div class="abs office" style="left:686px;top:3693px;display:flex;gap:18px"><div class="pin"><svg width="22" height="28" fill="var(--blue)"><path d="M11 0a10 10 0 0 1 10 10c0 7-10 18-10 18S1 17 1 10A10 10 0 0 1 11 0z"/><circle cx="11" cy="10" r="4" fill="#fff"/></svg></div><div><h6>CAMBRIDGE</h6><p>4th Floor Orrin House 12 Kestrel Row<br>Cambridge CB0 1AA</p></div></div>
<div class="abs office" style="left:686px;top:3816px;display:flex;gap:18px"><div class="pin"><svg width="22" height="28" fill="var(--blue)"><path d="M11 0a10 10 0 0 1 10 10c0 7-10 18-10 18S1 17 1 10A10 10 0 0 1 11 0z"/><circle cx="11" cy="10" r="4" fill="#fff"/></svg></div><div><h6>LONDON</h6><p>9th Floor Alder Court 40 Wren Lane<br>London EC0 2BB</p></div></div>
<div class="abs office" style="left:686px;top:3928px;display:flex;gap:18px"><div class="pin"><svg width="22" height="28" fill="var(--blue)"><path d="M11 0a10 10 0 0 1 10 10c0 7-10 18-10 18S1 17 1 10A10 10 0 0 1 11 0z"/><circle cx="11" cy="10" r="4" fill="#fff"/></svg></div><div><h6>SINGAPORE</h6><p>14th Floor Lumen Tower 8 Harbour Quay<br>Singapore 000128</p></div></div>

<!-- footer -->
<footer class="abs footer"></footer>
<div class="abs head" style="left:125px;top:4196px;font-weight:700;font-size:22px;color:#fff">Harlow Vectors</div>
<p class="abs" style="left:125px;top:4236px;width:310px;font-size:11px;line-height:17px;color:#9fb0c6">© 2021 Harlow Vectors. All rights reserved. Privacy Policy. Terms of Use.</p>
<div class="abs f-div" style="left:465px;top:4180px"></div>
<div class="abs f-col" style="left:509px;top:4182px"><h6>CONTACT US</h6><p>220 Marlow Lane<br>Fenwick 00120<br>Tel: (144) 555 0142<br>Email: hello@harlowvectors.example</p></div>
<div class="abs f-div" style="left:724px;top:4180px"></div>
<div class="abs f-col" style="left:760px;top:4182px"><h6>NAVIGATE</h6><p>Who we are<br>What we do<br>Culture<br>Blog<br>Resources<br>Contact us</p></div>
<div class="abs f-div" style="left:912px;top:4180px"></div>
<div class="abs f-col" style="left:952px;top:4182px"><h6>FOLLOW US</h6>
  <svg style="margin-top:12px" width="80" height="24"><circle cx="12" cy="12" r="11" fill="#9fb0c6"/><circle cx="40" cy="12" r="11" fill="#9fb0c6"/><circle cx="68" cy="12" r="11" fill="#9fb0c6"/></svg></div>

<!-- disclaimer -->
<div class="abs shade"></div>
<div class="abs modal">
  <div class="abs brand"><i></i>Harlow Vectors</div>
  <h2 class="abs m-title">HARLOW <span>VECTORS</span></h2>
  <p class="abs m-intro">Please read these Terms of Use (the "Terms") carefully before proceeding as they explain certain restrictions imposed by law on the distribution of the information on this website</p>
  <div class="abs terms">
    <div class="abs num">1.</div>
    <h4 class="abs">Harlow Vectors</h4>
    <p class="abs">Ais nostrud exercitation ullamco laboris nisi ut aliquip ex ea commodo consequat. Duis aute irure dolor in reprehenderit in voluptate velit esse cillum dolore eu fugiat nulla pariatur. Exceptemodo consequat. Duis ute irure dolor in reprehenderit in voluptate velit esse cillum dolore eu fugiat nulla pariatur.</p>
    <div class="abs scroll"><div style="margin:22px 1px 0;height:26px;background:var(--accent)"></div></div>
  </div>
  <div class="abs btn accept">I ACCEPT</div>
  <div class="abs btn decline">I DO NOT ACCEPT</div>
  <div class="abs cookies"><b>COOKIES CONTROL</b>This website uses cookies. By continuing to use this website you are giving consent to cookies being used.<br>For information on cookies, visit our Cookies Policy.</div>
</div>

</body>
</html>
```